Full Business Set-Up Stationary, Folder, Envelope, & Business Card, etc. CPA Firm
CPA Firm Collarteral Package
Full Business Set-Up Stationary, Folder, Envelope, & Business Card, etc. CPA Firm - Consulting
Creative Brief
Bright & Fun-filled
Marla Penn, CPA
Certified Public Accountant
512 Hadley Court Suite 200 Oakmere, FL 40217
MarlaPenn@ledgerbox.example
www.MarlaPennCPA.example
RT58163
Key Words: CPA since 1999 Servicing State of Florida since 1999 Certified Management Accountant Certified Public Accounting Firm Award Winning CPA Award Winning Professional Officies Located in the Oakmere Civic Trade Hall Trustworthy, Professional, Experienced
Tag Line: See the Clarity TrueMark Services
marlapenn marlapenn
Thanks for your submissions. Please include portfolio for the Firm. Particularly a Business Folder and Letterhead/Envelope. Ipad and Iphone Designs.

```html
<!DOCTYPE html>
<html lang="en">
<head>
<meta charset="utf-8">
<title>Marla Penn CPA — Business Card</title>
<link href="https://fonts.googleapis.com/css2?family=Cinzel:wght@400;600&family=EB+Garamond:wght@400;500&display=swap" rel="stylesheet">
<style>
  :root {
    --stage: #7a7c80;
    --brand-blue: #2a7fd4;
    --brand-blue-deep: #1663b8;
    --brand-blue-light: #4d9be6;
    --accent-green: #7cc242;
    --paper: #ffffff;
    --ink: #2a5f9e;
    --ink-soft: #3a6fae;
  }
  * { box-sizing: border-box; margin: 0; padding: 0; }
  html, body { width: 1200px; height: 908px; overflow: hidden; }
  body {
    background: var(--stage);
    display: flex;
    align-items: center;
    justify-content: center;
    gap: 48px;
    font-family: "EB Garamond", serif;
  }
  .card {
    position: relative;
    width: 540px;
    height: 310px;
    border-radius: 18px;
    overflow: hidden;
    box-shadow: 0 10px 24px rgba(0,0,0,0.25);
  }
  /* Front */
  .card--front {
    background: linear-gradient(135deg, var(--brand-blue-light) 0%, var(--brand-blue) 45%, var(--brand-blue-deep) 100%);
    color: var(--paper);
  }
  .front__brand {
    position: absolute;
    left: 40px;
    top: 118px;
  }
  .front__name {
    font-family: "Cinzel", serif;
    font-size: 34px;
    font-weight: 400;
    letter-spacing: 0.5px;
    line-height: 1;
  }
  .front__tagline {
    font-family: "Cinzel", serif;
    font-size: 11px;
    letter-spacing: 5px;
    margin-top: 8px;
  }
  /* Back */
  .card--back { background: var(--paper); }
  .back__shape { position: absolute; inset: 0; }
  .back__title {
    position: absolute;
    right: 26px;
    top: 82px;
    text-align: right;
    color: var(--paper);
  }
  .back__title-name {
    font-family: "Cinzel", serif;
    font-size: 19px;
  }
  .back__title-role {
    font-family: "Cinzel", serif;
    font-size: 10px;
    letter-spacing: 1px;
    margin-top: 4px;
  }
  .back__brand {
    position: absolute;
    left: 30px;
    top: 50px;
    display: flex;
    align-items: center;
    gap: 10px;
    color: var(--ink);
  }
  .brand-dot {
    width: 30px; height: 30px;
    border-radius: 50%;
    background: var(--accent-green);
  }
  .back__brand-name {
    font-family: "Cinzel", serif;
    font-size: 22px;
    line-height: 1;
  }
  .back__brand-tagline {
    font-family: "Cinzel", serif;
    font-size: 8px;
    letter-spacing: 3.5px;
    margin-top: 5px;
  }
  .back__contact {
    position: absolute;
    left: 30px;
    top: 140px;
    list-style: none;
    color: var(--ink-soft);
    font-size: 14px;
    line-height: 1.32;
  }
  .back__license {
    font-size: 12px;
    color: var(--accent-green);
    margin-bottom: 6px;
    list-style: none;
  }
  .back__contact li { display: flex; align-items: center; gap: 8px; }
  .bullet {
    width: 8px; height: 8px;
    border-radius: 50%;
    background: var(--accent-green);
    flex: none;
  }
</style>
</head>
<body>

  <section class="card card--front" aria-label="Business card front">
    <div class="front__brand">
      <div class="front__name">Marla Penn CPA</div>
      <div class="front__tagline">SEE THE CLARITY</div>
    </div>
  </section>

  <section class="card card--back" aria-label="Business card back">
    <svg class="back__shape" viewBox="0 0 540 310" preserveAspectRatio="none" aria-hidden="true">
      <path d="M350 0 C 300 90, 300 210, 330 310 L 540 310 L 540 0 Z" fill="var(--accent-green)"/>
      <path d="M362 0 C 316 90, 316 210, 346 310 L 540 310 L 540 0 Z" fill="var(--brand-blue)"/>
    </svg>

    <div class="back__title">
      <div class="back__title-name">Marla Penn, CPA</div>
      <div class="back__title-role">CERTIFIED PUBLIC ACCOUNTANT</div>
    </div>

    <div class="back__brand">
      <span class="brand-dot"></span>
      <div>
        <div class="back__brand-name">Marla Penn CPA</div>
        <div class="back__brand-tagline">SEE THE CLARITY</div>
      </div>
    </div>

    <ul class="back__contact">
      <li class="back__license">License No. RT58163</li>
      <li><span class="bullet"></span>512 Hadley Court Suite 200</li>
      <li><span class="bullet"></span>Oakmere, FL 40217</li>
      <li><span class="bullet"></span>555.201.3480</li>
      <li><span class="bullet"></span>555.201.7731</li>
      <li><span class="bullet"></span>MarlaPenn@ledgerbox.example</li>
      <li><span class="bullet"></span>www.MarlaPennCPA.example</li>
    </ul>
  </section>

</body>
</html>
```